Web presentation for K.teravinu & Partners A Professional Law Corporation

To design a full detailed web presentation for the above mentioned corporation.

It Professional

```html
<!DOCTYPE html>
<html lang="en">
<head>
<meta charset="utf-8">
<title>K.teravinu &amp; Partners – Professional Law Corporation</title>
<link rel="stylesheet" href="https://fonts.googleapis.com/css2?family=Tinos:wght@400;700&family=Arimo:wght@400;700&display=swap">
<style>
:root{
  --navy:#1c2d57;
  --navy-deep:#16244a;
  --gold:#d4a52a;
  --gold-dark:#b98d1c;
  --panel:#dde3ef;
  --ink:#1a1a1a;
  --muted:#555;
  --rule:#c8c8c8;
  --footer-bg:#f1f1f1;
}
*{box-sizing:border-box;margin:0;padding:0}
html,body{width:1200px;height:2748px;overflow:hidden;background:#fff}
body{position:relative;font-family:"Arimo",Arial,sans-serif;color:var(--ink)}
.abs{position:absolute}
.serif{font-family:"Tinos","Times New Roman",serif}

/* header */
.brand{left:357px;top:12px;width:486px;height:86px;display:flex;align-items:center;gap:18px}
.brand-square{width:86px;height:86px;background:var(--navy);border:4px solid var(--gold);flex:none}
.brand-name{font-family:"Tinos",serif;font-weight:700;color:var(--navy);font-size:33px;letter-spacing:3px;line-height:1.05}
.brand-name small{display:block;font-size:19px;letter-spacing:2px}

.nav{left:0;top:119px;width:1200px;height:58px;display:flex;align-items:center;font-family:"Tinos",serif;font-size:21px;color:var(--ink)}
.nav a{color:inherit;text-decoration:none;padding:0 26px}
.nav a.active{background:var(--gold);color:#fff;height:58px;line-height:58px;padding:0 30px;margin-right:12px}
.nav-rule{left:0;top:176px;width:1200px;height:4px;background:var(--navy)}
.nav-rule2{left:0;top:182px;width:1200px;height:2px;background:var(--navy)}

.search{left:15px;top:197px;width:238px;height:24px;background:#dfe5ef;border-radius:4px}
.search svg{position:absolute;left:8px;top:4px}
.scope{left:264px;top:197px;width:176px;height:24px;border:1px solid #9aa;font-size:14px;padding:3px 6px;background:#fff}
.select-arrow{position:absolute;right:2px;top:2px;width:18px;height:18px;background:#c9d6ec}
.util{top:201px;font-family:"Tinos",serif;font-size:16px}
.lang{left:1078px;top:197px;width:112px;height:24px;border:1px solid #9aa;font-size:14px;padding:3px 6px}

/* hero */
.hero{left:0;top:253px;width:1200px;height:364px;background:linear-gradient(90deg,#4a2f22 0%,#6d4b37 25%,#8c7460 45%,#b7a28c 60%,#5b4a3e 80%,#3a2a22 100%)}
.hero-caption{left:110px;top:361px;width:407px;height:179px;background:rgba(28,45,87,.92);color:#fff;padding:16px 14px}
.hero-caption h1{font-family:"Tinos",serif;font-weight:400;font-size:37px;line-height:1.1}
.hero-caption p{font-family:"Tinos",serif;font-size:26px;line-height:1.2;margin-top:6px}
.hero-arrow{top:416px;width:55px;height:55px;background:rgba(0,0,0,.35);display:flex;align-items:center;justify-content:center}
.dot{top:578px;width:17px;height:17px;border-radius:50%;background:var(--gold)}

/* tabs */
.tab{top:660px;height:62px;border:2px solid var(--gold);font-family:"Tinos",serif;font-weight:700;font-size:21px;color:var(--navy);display:flex;align-items:center;justify-content:center}
.tab.active{background:var(--navy);color:#fff;border-color:var(--navy)}

/* news */
.news{left:15px;width:824px;height:120px}
.news-date{position:absolute;left:0;top:6px;font-size:15px}
.badge{position:absolute;left:135px;top:0;width:143px;height:33px;color:#fff;font-weight:700;font-size:16px;display:flex;align-items:center;justify-content:center}
.badge.seminar{background:var(--gold)}
.badge.news-b{background:var(--navy)}
.news-title{position:absolute;left:298px;top:2px;width:530px;font-weight:700;font-size:17px;line-height:1.25;color:var(--navy)}
.news-author{position:absolute;left:298px;font-weight:700;font-size:16px;color:var(--navy)}
.btn{background:var(--gold);color:#fff;font-size:17px;display:flex;align-items:center;justify-content:center}

/* sidebar */
.side{left:857px;width:336px;background:var(--panel)}
.side.ruled{border-top:4px solid var(--navy)}
.side h3{font-family:"Tinos",serif;font-weight:700;color:var(--navy);font-size:21px;text-align:center}
.side ul{list-style:none;font-size:17px;color:var(--navy)}
.side li::before{content:"▸ ";font-size:13px}
.career-date{font-size:15px;color:#333}
.career-link{font-size:17px;font-weight:700;color:var(--navy);line-height:1.25}

/* lower sections */
.divider{left:13px;top:1886px;width:1174px;height:1px;background:#ddd;box-shadow:0 6px 10px rgba(0,0,0,.08)}
.col-title{top:1950px;font-family:"Tinos",serif;font-weight:700;font-size:20px;color:var(--navy);border-bottom:1px solid #a89a7c;padding-bottom:12px}
.frame{top:2015px;height:193px;background:#fff;border:1px solid #e2e2e2;box-shadow:0 2px 6px rgba(0,0,0,.15);padding:8px}
.frame div{width:100%;height:100%}
.col-text{top:2228px;font-size:15px;line-height:1.55;color:#333}
.quote-text{left:835px;top:2076px;width:343px;font-size:15px;line-height:1.55;color:#444}

/* footer */
.footer{left:0;top:2394px;width:1200px;height:292px;background:var(--footer-bg)}
.foot-brand{left:13px;top:2391px;width:210px;height:137px;background:#fff;box-shadow:0 2px 8px rgba(0,0,0,.15);display:flex;align-items:center;justify-content:center;gap:10px}
.foot-brand .brand-square{width:40px;height:40px;border-width:3px}
.foot-brand span{font-family:"Tinos",serif;font-weight:700;color:var(--navy);font-size:20px}
.field{border:1px solid #ccc;background:#fff;font-size:15px;color:#666;padding:6px 8px}
.contact p{font-size:14px;line-height:1.85;color:#333}
.contact b{color:#222}
.bottom-bar{left:0;top:2686px;width:1200px;height:62px;background:var(--navy);color:#fff;font-size:15px}
.to-top{left:1106px;top:2364px;width:60px;height:60px;border-radius:50%;background:#666;border:4px solid #ddd;display:flex;align-items:center;justify-content:center}
</style>
</head>
<body>

<header>
  <div class="abs brand">
    <div class="brand-square"></div>
    <div class="brand-name">K. TERAVINU<small>&amp; PARTNERS · Professional Law Corporation</small></div>
  </div>

  <nav class="abs nav">
    <a class="active">Home</a>
    <a>Profile</a>
    <a>Practice Areas</a>
    <a>Sectors</a>
    <a>Institute of advanced legal studies</a>
    <a>Center of legal Translation</a>
  </nav>
  <div class="abs nav-rule"></div>
  <div class="abs nav-rule2"></div>

  <div class="abs search">
    <svg width="18" height="18" viewBox="0 0 18 18"><circle cx="7" cy="7" r="5" fill="none" stroke="#1c2d57" stroke-width="2.5"/><line x1="11" y1="11" x2="16" y2="16" stroke="#1c2d57" stroke-width="3"/></svg>
  </div>
  <div class="abs scope">Search Entire Site<span class="select-arrow"></span></div>
  <div class="abs util" style="left:600px">▸ Career and general inquiries</div>
  <div class="abs util" style="left:836px">▸ Location</div>
  <div class="abs util" style="left:938px">▸ Contact Us</div>
  <div class="abs lang">Language<span class="select-arrow"></span></div>
</header>

<section>
  <div class="abs hero" role="img" aria-label="Portrait of a lawyer in a suit in front of law library bookshelves"></div>
  <div class="abs hero-caption">
    <h1>teravinupartners.com</h1>
    <p>Our team does not promise you more than you deserve, but we will not settle for less.</p>
  </div>
  <div class="abs hero-arrow" style="left:22px"><svg width="16" height="22"><path d="M12 3 4 11l8 8" fill="none" stroke="#fff" stroke-width="3"/></svg></div>
  <div class="abs hero-arrow" style="left:1112px"><svg width="16" height="22"><path d="M4 3l8 8-8 8" fill="none" stroke="#fff" stroke-width="3"/></svg></div>
  <div class="abs dot" style="left:181px;background:#fff"></div>
  <div class="abs dot" style="left:206px"></div>
  <div class="abs dot" style="left:230px"></div>
</section>

<main>
  <div class="abs tab active" style="left:11px;width:192px">Latest Information</div>
  <div class="abs tab" style="left:216px;width:194px">Seminars</div>
  <div class="abs tab" style="left:421px;width:195px">Publications</div>
  <div class="abs tab" style="left:627px;width:194px">Topics</div>

  <article class="abs news" style="top:760px">
    <span class="news-date">August 31, 2017</span><span class="badge seminar">Seminars</span>
    <p class="news-title">Teravinupartners.com Available On-Demand (until August 31, 2017)<br>Update on Japanese Pharma Regulations</p>
    <p class="news-author" style="top:84px">Haruto Ishida &nbsp;(Dubai)</p>
  </article>
  <article class="abs news" style="top:914px">
    <span class="news-date">August 2, 2017</span><span class="badge news-b">News</span>
    <p class="news-title">Comparison and Practical Analysis of Real Estate related Security and Enforcement Procedures in Asia-Pacific countries</p>
    <p class="news-author" style="top:62px">Takeshi Mori</p>
  </article>
  <div class="abs" style="left:0;top:1082px;width:839px;height:1px;background:#e6e6e6"></div>
  <article class="abs news" style="top:1048px">
    <span class="news-date">August 31, 2017</span><span class="badge seminar">Seminars</span>
    <p class="news-title">Teravinupartners.com Available On-Demand (until August 31, 2017)<br>Update on Japanese Pharma Regulations</p>
    <p class="news-author" style="top:84px">Haruto Ishida &nbsp;(Dubai)</p>
  </article>
  <article class="abs news" style="top:1200px">
    <span class="news-date">August 2, 2017</span><span class="badge news-b">News</span>
    <p class="news-title">Comparison and Practical Analysis of Real Estate related Security and Enforcement Procedures in Asia-Pacific countries</p>
    <p class="news-author" style="top:62px">Takeshi Mori</p>
  </article>
  <article class="abs news" style="top:1328px">
    <span class="news-date">August 31, 2017</span><span class="badge seminar">Seminars</span>
    <p class="news-title">Teravinupartners.com Available On-Demand (until August 31, 2017)<br>Update on Japanese Pharma Regulations</p>
    <p class="news-author" style="top:84px">Haruto Ishida &nbsp;(Dubai)</p>
  </article>
  <article class="abs news" style="top:1480px">
    <span class="news-date">August 2, 2017</span><span class="badge news-b">News</span>
    <p class="news-title">Comparison and Practical Analysis of Real Estate related Security and Enforcement Procedures in Asia-Pacific countries</p>
    <p class="news-author" style="top:62px">Takeshi Mori</p>
  </article>
  <div class="abs btn" style="left:725px;top:1659px;width:109px;height:30px">Read More...</div>
</main>

<aside>
  <div class="abs side" style="top:660px;height:95px;padding:12px 14px;font-family:'Tinos',serif;font-size:16px;color:var(--navy);line-height:1.45">
    <b>[Important Notice]</b><br>Please be Careful of Fraud that uses the Name of our Office or Attorneys
  </div>

  <div class="abs side ruled" style="top:777px;height:319px">
    <h3 style="margin-top:26px">Overseas Practice</h3>
    <div style="margin:22px 16px 0;height:1px;background:#fff"></div>
    <div class="abs" role="img" aria-label="Pale globe map illustration" style="right:0;bottom:0;width:110px;height:120px;background:radial-gradient(circle at 80% 70%,#a9c6e2,rgba(221,227,239,0) 70%)"></div>
    <ul style="position:absolute;left:18px;top:100px;line-height:31px">
      <li>Divotce Service</li><li>Citizenship &amp; Residence</li><li>Individual Investor Programme</li>
      <li>Arbitration and ADR</li><li>Civil Litigation</li><li>Criminal Defence</li><li>Commercial and Corporate</li>
    </ul>
  </div>

  <div class="abs side ruled" style="top:1119px;height:178px">
    <h3 style="margin-top:22px;font-size:19px">Teravinupartners.com</h3>
    <p class="serif" style="text-align:center;font-size:14px;color:var(--navy);margin-top:4px">Available On-Demand</p>
    <div style="margin:14px 16px 0;height:1px;background:#fff"></div>
    <ul style="margin:16px 0 0 18px;line-height:31px"><li>Update on Arab<br>&nbsp;&nbsp;&nbsp;Pharma Regulations</li></ul>
  </div>

  <div class="abs side ruled" style="top:1321px;height:108px">
    <div class="abs" role="img" aria-label="Stack of newspapers" style="right:0;top:0;width:150px;height:104px;background:linear-gradient(90deg,rgba(221,227,239,0),#c9ced8 55%,#9ea6b4)"></div>
    <h3 class="abs" style="left:14px;top:26px;text-align:left;font-size:20px;line-height:1.2">Teravinupartners.com<br>Newsletter</h3>
  </div>

  <div class="abs side ruled" style="top:1451px;height:392px;padding:0 18px">
    <h3 style="margin-top:26px">Career</h3>
    <div style="margin:16px 0 18px;height:1px;background:#fff"></div>
    <p class="career-date">May 25, 2017</p>
    <p class="career-link">▸ 2017 Internship Program in<br>&nbsp;&nbsp;Teravinupartners Bangkok Office</p>
    <p class="career-date" style="margin-top:20px">July 6, 2017</p>
    <p class="career-link">▸ Career opportunity in<br>&nbsp;&nbsp;Teravinupartners Office (Lawyer)</p>
    <p class="career-date" style="margin-top:20px">June 28, 2017</p>
    <p class="career-link">▸ Career opportunity in<br>&nbsp;&nbsp;Teravinupartners Bangkok Office<br>&nbsp;&nbsp;(Lawyer)</p>
  </div>
</aside>

<section>
  <div class="abs divider"></div>

  <h2 class="abs col-title" style="left:24px;width:342px">Our firm</h2>
  <div class="abs frame" style="left:24px;width:342px"><div role="img" aria-label="Lawyer reviewing a document before a courtroom audience" style="background:linear-gradient(135deg,#c9a88a,#7a5b45 55%,#3b2a20)"></div></div>
  <p class="abs col-text" style="left:24px;width:342px">Lorem ipsum dolor sit amet, consectetur adipiscing elit. Morbi id tristique sem. Nunc nec ipsum sed nisi dictum mollis.</p>
  <div class="abs btn" style="left:24px;top:2312px;width:110px;height:30px">Read More...</div>

  <h2 class="abs col-title" style="left:429px;width:342px">K.teravinu &amp; Partners</h2>
  <div class="abs frame" style="left:429px;width:342px"><div role="img" aria-label="Senior partner seated at his office desk" style="background:linear-gradient(135deg,#e2dfe0,#a39a98 50%,#5a3e38)"></div></div>
  <p class="abs col-text" style="left:429px;width:342px">Morbi id tristique sem. Nunc nec ipsum sed nisi dictum mollis. Praesent malesuada mauris a odio adipiscing mollis.</p>
  <div class="abs btn" style="left:429px;top:2312px;width:110px;height:30px">Read More...</div>

  <h2 class="abs col-title" style="left:835px;width:343px">What Client’s Say</h2>
  <svg class="abs" style="left:835px;top:2015px" width="44" height="34" viewBox="0 0 44 34"><path d="M2 2h17v16l-8 14H4l6-14H2zM24 2h17v16l-8 14h-7l6-14h-8z" fill="#cfcfcf"/></svg>
  <p class="abs quote-text">“ Nunc nec ipsum sed nisi dictum mollis. Praesent malesuada mauris a odio adipiscing mollis. In varius tincidunt elit vitae eleifend. Etiam fermentum suscipit est vel aliquet. ”</p>
  <div class="abs" style="left:835px;top:2171px;width:343px;height:1px;background:#ddd"></div>
  <div class="abs frame" style="left:839px;top:2184px;width:125px;height:115px;padding:4px"><div role="img" aria-label="Smiling family of four outdoors" style="background:linear-gradient(135deg,#e9c9a2,#b88864 50%,#7a9a4a)"></div></div>
  <p class="abs" style="left:978px;top:2190px;font-size:15px;font-style:italic;color:#444;line-height:1.55">Clara Venn,<br>Director of<br><span style="color:#888">Northgate Homes</span></p>
</section>

<footer>
  <div class="abs footer"></div>
  <div class="abs to-top"><svg width="24" height="16"><path d="M3 13l9-9 9 9" fill="none" stroke="#fff" stroke-width="4"/></svg></div>
  <div class="abs foot-brand"><div class="brand-square"></div><span>K. Teravinu</span></div>

  <p class="abs" style="left:13px;top:2584px;font-size:13px;color:#555">Social Network</p>
  <div class="abs" style="left:115px;top:2582px;display:flex;gap:4px">
    <span style="width:18px;height:18px;background:#e8873a"></span>
    <span style="width:18px;height:18px;background:#3b5a9a"></span>
    <span style="width:18px;height:18px;background:#9aa3ad"></span>
    <span style="width:18px;height:18px;background:#49a9e0"></span>
    <span style="width:18px;height:18px;background:#4a7fb0"></span>
    <span style="width:18px;height:18px;background:#d8d8d8"></span>
  </div>

  <h3 class="abs serif" style="left:354px;top:2420px;font-size:20px;color:var(--navy)">Career and general inquiries</h3>
  <div class="abs field" style="left:348px;top:2468px;width:211px;height:33px">Name</div>
  <div class="abs field" style="left:348px;top:2515px;width:211px;height:33px">Email</div>
  <div class="abs field" style="left:348px;top:2566px;width:211px;height:33px">Address</div>
  <div class="abs field" style="left:579px;top:2468px;width:209px;height:130px">Message</div>
  <div class="abs btn" style="left:581px;top:2616px;width:145px;height:35px">Send Message</div>

  <div class="abs contact" style="left:879px;top:2420px;width:300px">
    <h3 class="serif" style="font-size:20px;color:var(--navy);margin-bottom:8px">Contact</h3>
    <p><b>Address: K.teravinu &amp; Partners</b><br>218 Alder Lane,<br>Fairview, CA 94000</p>
    <p style="margin-top:8px"><b>Phone:</b> (555) 014-2290</p>
    <p style="margin-top:8px"><b>Fax:</b> (555) 014-2291</p>
    <p style="margin-top:8px"><b>Email:</b> info@teravinupartners.com</p>
  </div>

  <div class="abs bottom-bar">
    <p class="abs" style="left:11px;top:21px">© 2017 Copyright <b>Teravinupartners.com</b>. All Rights Reserved</p>
    <p class="abs" style="left:556px;top:21px">Home &nbsp;| &nbsp;Profile &nbsp;| &nbsp;Practice Areas &nbsp;| &nbsp;Sectors &nbsp;| &nbsp;Institute of advanced legal studies &nbsp;| &nbsp;Contact Us</p>
  </div>
</footer>

</body>
</html>
```